Wordpress web design

We need a website buil in using Wordpress with 5 pages.

Pages: HOME SERVICES GALLERY TESTIMONIALS CONTACT US ABOUT US.

We are looking for a unique, professional and clean web for our construction company.

Company name: TALL OAK BUILDING SERVICES. We can olso provide you with the logo. Please don't use any flashin, intro, or any ready templates.

All your ideas are welcome.

Many thanks,
Dorian

Target Market(s)

Construction

Industry/Entity Type

Construction

Font styles to use
Sans Serif
Decorative

Requirements
Must have
• Connect with construction and London
Nice to have
• Nice and clean

```html
<!DOCTYPE html>
<html lang="en">
<head>
<meta charset="utf-8">
<title>Tall Oak Building Services</title>
<link href="https://fonts.googleapis.com/css2?family=Cinzel:wght@400;600&family=Lato:ital,wght@0,400;0,700;1,400&display=swap" rel="stylesheet">
<style>
:root{
  --blue:#29b3ec;
  --blue-dark:#1a9bd6;
  --ink:#222;
  --body:#3a3a3a;
  --red:#c4161c;
  --paper:#f2f0ec;
  --white:#fff;
  --grey:#6c6c6c;
}
*{margin:0;padding:0;box-sizing:border-box}
html,body{width:827px;height:1200px;overflow:hidden}
body{position:relative;font-family:'Lato',sans-serif;color:var(--body);background:var(--paper)}
.abs{position:absolute}
.caps{font-family:'Cinzel',serif;font-weight:400}

.hero{left:0;top:0;width:827px;height:316px;background:linear-gradient(180deg,#9bb3dd 0%,#c9cfe4 45%,#a79a88 75%,#6d5e4c 100%)}
.brand{left:90px;top:22px;font-family:'Lato',sans-serif;font-weight:700;font-size:20px;color:var(--ink);letter-spacing:1px;display:flex;align-items:center;gap:6px}
.brand i{display:block;width:14px;height:14px;background:var(--red)}
.top-phone{left:632px;top:10px;font-size:13px;color:#333;display:flex;align-items:center;gap:6px}
.tagline{left:446px;top:236px;width:290px;height:50px;background:rgba(20,20,20,.78);padding:2px 0 0 34px;font-family:'Cinzel',serif;font-size:17.5px;line-height:22px;letter-spacing:.5px;color:#fff}
.tagline span{color:var(--blue)}

.nav{left:0;top:316px;width:827px;height:29px;background:var(--blue);display:flex;padding-left:90px}
.nav a{font-family:'Cinzel',serif;font-size:12.5px;color:#fff;text-decoration:none;line-height:29px;padding:0 28px;border-right:1px solid rgba(255,255,255,.35)}
.nav a:last-child{border:none}
.nav a.active{background:#f3f3f3;color:#333;padding:0 18px}

.welcome{left:92px;top:384px;width:432px}
.welcome h1{font-family:'Cinzel',serif;font-weight:400;font-size:19px;color:var(--ink);white-space:nowrap}
.welcome h1 span{color:var(--blue)}
.welcome .lead{margin-top:10px;font-weight:700;font-size:9.6px;line-height:15px;color:#222}
.welcome p{margin-top:4px;font-size:9.6px;line-height:15.5px}
.read{color:var(--red);font-size:9.6px;font-weight:700;margin-top:8px;display:block}
.divider{left:538px;top:388px;width:1px;height:176px;background:#ddd}

.testi{left:556px;top:384px;width:181px}
.testi h2{font-family:'Cinzel',serif;font-weight:400;font-size:17px;color:var(--blue);display:flex;align-items:center;gap:6px;padding-bottom:4px;border-bottom:1px solid #d0d0d0}
.avatar{left:0;top:30px;width:60px;height:60px;border-radius:50%;border:3px solid #ddd;background:radial-gradient(circle at 50% 40%,#c99b7c,#6a4d3a)}
.who{left:71px;top:48px;font-size:9.6px;color:#222;font-weight:700}
.who small{display:block;font-weight:400;font-size:8.4px;color:#555;margin-top:3px}
.quote{left:0;top:100px;width:181px;height:73px;background:#fff;border:1px solid #e2e2e2;padding:8px 8px 0 10px;font-style:italic;font-size:9px;line-height:15.5px;color:#444}
.dots{right:10px;bottom:6px;display:flex;gap:3px}
.dots b{width:5px;height:5px;border-radius:50%;background:#ccc}
.dots b.on{background:var(--red)}

.band-white{left:0;top:583px;width:827px;height:252px;background:#fbfaf8;border-top:1px solid #e4e2dd}
.card{top:609px;width:200px;height:193px;background:#f4f3f1;border:1px solid #cfcfcf;border-radius:3px;box-shadow:0 6px 6px -4px rgba(0,0,0,.25)}
.card .ph{position:absolute;left:5px;top:5px;width:188px;height:90px;border-radius:3px}
.card h3{position:absolute;left:8px;top:100px;font-family:'Cinzel',serif;font-weight:400;font-size:14.5px;color:var(--blue);white-space:nowrap}
.card p{position:absolute;left:8px;top:130px;width:180px;font-size:8.8px;line-height:13px;color:#444;padding-bottom:6px;border-bottom:1px solid #dcdcdc}
.card .read{position:absolute;left:10px;top:170px;font-weight:400;font-size:8.8px;margin:0}

.gallery-band{left:0;top:835px;width:827px;height:171px;background:#efedea;border-top:1px solid #d6d4d0}
.gal-tab{left:310px;top:0;width:210px;height:24px;background:#6a6a6a;clip-path:polygon(0 0,100% 0,93% 100%,7% 100%);text-align:center;font-family:'Cinzel',serif;font-size:16px;color:#fff;line-height:24px}
.shot{top:48px;width:142px;height:97px}
.shot .cap{position:absolute;left:0;bottom:0;width:100%;height:25px;background:rgba(0,0,0,.7);color:#fff;font-size:9.6px;line-height:25px;padding-left:7px}
.arrow{top:84px;width:20px;height:20px;border-radius:50%;border:1.5px solid #bbb;background:#f5f5f5}

.footer{left:0;top:1006px;width:827px;height:194px;background:var(--blue);color:#fff}
.footer h4{position:absolute;top:12px;font-family:'Cinzel',serif;font-weight:400;font-size:13px}
.footer .rule{position:absolute;left:0;top:40px;width:827px;border-top:1px dashed rgba(0,0,0,.35)}
.links{left:92px;top:52px;list-style:none;font-size:8.8px}
.links li{height:23.4px;padding-left:10px;position:relative}
.links li::before{content:'›';position:absolute;left:0;top:-2px}
.contact{left:240px;top:52px;font-size:8.8px;line-height:14px}
.contact .row{display:flex;align-items:center;gap:6px;margin-top:16px}
.field{left:403px;width:151px;height:20px;background:#bfe8f8;border:1px solid #7a8a90;font-size:8.8px;color:#444;padding:4px 6px}
.submit{left:403px;top:158px;width:67px;height:20px;background:#555;color:#fff;font-weight:700;font-size:10px;text-align:center;line-height:20px;border:1px solid #333}
.social{left:616px;top:8px;display:flex;gap:6px}
.social b{width:21px;height:21px;border-radius:50%;border:2px solid #fff}
.f-brand{left:602px;top:100px;width:130px;text-align:center;font-weight:700;font-size:18px;letter-spacing:1px}
.copy{left:590px;top:155px;width:150px;text-align:center;font-size:8.8px;line-height:13px}
</style>
</head>
<body>

<div class="abs hero" role="img" aria-label="Photo of a large two-storey family house with grey siding and lit windows at dusk"></div>
<div class="abs brand"><i></i>TALL OAK</div>
<div class="abs top-phone">
  <svg width="18" height="18" viewBox="0 0 20 20"><circle cx="10" cy="10" r="9" fill="none" stroke="#333" stroke-width="1.3"/><path d="M6.5 5.5l2 0 .8 2.3-1.2 1a6 6 0 0 0 3 3l1-1.2 2.3.8v2c-4.5.5-8.4-3.4-7.9-7.9z" fill="#333"/></svg>
  555-210-4477
</div>
<div class="abs tagline">WE ARE A FULL SERVICE<br><span>CONSTRUCTION COMPANY</span></div>

<nav class="abs nav">
  <a class="active">Home</a><a>Services</a><a>Gallery</a><a>Testimonials</a><a>About Us</a><a>Contact Us</a>
</nav>

<section class="abs welcome">
  <h1>Welcome to <span>Tall Oak Building Services</span></h1>
  <p class="lead">Lorem ipsum dolor sit amet, consectetuer adipiscing elit, sed diam nonummy nibh euismod tincidl untm ut laoreet dolore magna aliquam erat volutpat.</p>
  <p>Lorem ipsum dolor sit amet, consectetuer adipiscing elit, sed diam nonummy nibh euismod tinciduntm ut laoreet dolore magna aliquam erat volutpat. Ut wisi enim ad minim veniam, quis nostrud exerciosgi tation ullamcorper suscipit lobortis nisl ut aliquip ex ea commodo consequat. Duis autem vel eumsodn iriure dolor in hendrerit in vulputate velit esse molestie consequat, vel illum dolore eu feugiat nullamo facilisis at vero eros et accumsan et iusto odio dignissim qui blandit praesent luptatum zzril delenitml augue duis dolore te feugait nulla facilisi.</p>
  <span class="read">Read More »</span>
</section>
<div class="abs divider"></div>

<aside class="abs testi">
  <h2><svg width="20" height="18" viewBox="0 0 20 18"><rect x="0" y="0" width="14" height="10" rx="2" fill="#c4161c"/><path d="M3 10l0 4 4-4z" fill="#c4161c"/><rect x="7" y="6" width="13" height="9" rx="2" fill="#29b3ec"/><path d="M16 15l0 3-3-3z" fill="#29b3ec"/></svg>Testimonials</h2>
  <div class="abs avatar" role="img" aria-label="Client portrait"></div>
  <div class="abs who">Marcus Hale<small>Bussiness Man</small></div>
  <div class="abs quote">“ Ut wisi enim ad minim veniam, quism nostrli erci tation ullamcorper suscipitop lobortis commodo consequat. ”
    <div class="abs dots"><b></b><b class="on"></b><b></b><b></b></div>
  </div>
</aside>

<div class="abs band-white"></div>
<article class="abs card" style="left:91px">
  <div class="ph" role="img" aria-label="Photo of a suburban residential house" style="background:linear-gradient(180deg,#6fa2d8,#c9b69a 60%,#5a6a3a)"></div>
  <h3>Residential Projects</h3>
  <p>Lorem ipsum dolor sit amet, consectetuer adipiscing elit, sed diam Lorem ipsum</p>
  <span class="read">Read More »</span>
</article>
<article class="abs card" style="left:314px">
  <div class="ph" role="img" aria-label="Photo of glass office towers against blue sky" style="background:linear-gradient(135deg,#2e5c9a,#7fb4e6 55%,#4d6b3a)"></div>
  <h3>Commercial Projects</h3>
  <p>Lorem ipsum dolor sit amet, consectetuer adipiscing elit, sed diam Lorem ipsum</p>
  <span class="read">Read More >></span>
</article>
<article class="abs card" style="left:537px">
  <div class="ph" role="img" aria-label="Photo of builders reviewing plans on a construction site" style="background:linear-gradient(180deg,#c9a24c,#8a7660 55%,#5a5048)"></div>
  <h3>Property Management</h3>
  <p>Lorem ipsum dolor sit amet, consectetuer adipiscing elit, sed diam Lorem ipsum</p>
  <span class="read">Read More >></span>
</article>

<section class="abs gallery-band">
  <div class="abs gal-tab">Project Gallery</div>
  <div class="abs arrow" style="left:90px"></div>
  <div class="abs shot" style="left:116px;background:linear-gradient(180deg,#8aa0b4,#4a3b2e 60%,#2a2520)" role="img" aria-label="Photo of a modern timber house at dusk">
    <div class="cap">Lorem ipsum dolor sit <svg style="position:absolute;right:8px;top:8px" width="10" height="9" viewBox="0 0 10 9"><path d="M0 4.5h8M5 1l3.5 3.5L5 8" stroke="#fff" stroke-width="1.8" fill="none"/></svg></div>
  </div>
  <div class="abs shot" style="left:267px;background:linear-gradient(180deg,#e8eef4,#4a78b0 50%,#2c3e5c)" role="img" aria-label="Photo of a glass office building"></div>
  <div class="abs shot" style="left:418px;background:linear-gradient(180deg,#9fc4ea,#6a6462 55%,#4f5a3a)" role="img" aria-label="Photo of a stone family home with garages"></div>
  <div class="abs shot" style="left:568px;background:linear-gradient(180deg,#a8c6e4,#9a5a40 55%,#3a3a38)" role="img" aria-label="Photo of a row of brick townhouses"></div>
  <div class="abs arrow" style="left:716px"></div>
</section>

<footer class="abs footer">
  <h4 style="left:92px">Quick Links</h4>
  <h4 style="left:240px">Contact Details</h4>
  <h4 style="left:404px">Quick Contact</h4>
  <div class="abs social"><b style="background:#3b5a9a"></b><b style="background:#3bb0e6"></b><b style="background:#d32a2a"></b><b style="background:#f07a1a"></b></div>
  <div class="rule"></div>
  <ul class="abs links"><li>Home</li><li>Services</li><li>Gallery</li><li>Testimonials</li><li>About Us</li><li>Contact Us</li></ul>
  <div class="abs contact">
    <b>123 Street Name,<br>&nbsp;City Name,</b> State Name,<br>Country Name - 123456
    <div class="row"><svg width="9" height="9" viewBox="0 0 10 10"><path d="M1 1h3l1 2.5-1.5 1a5 5 0 0 0 3 3l1-1.5L10 6v3C5 9.5.5 5 1 1z" fill="#fff"/></svg>555-210-4477</div>
    <div class="row"><svg width="10" height="9" viewBox="0 0 10 9"><rect x="2" y="0" width="6" height="3" fill="#fff"/><rect x="0" y="3" width="10" height="4" fill="#fff"/><rect x="2" y="6" width="6" height="3" fill="#fff"/></svg>555-210-4477</div>
    <div class="row"><svg width="10" height="7" viewBox="0 0 10 7"><rect width="10" height="7" fill="#fff"/><path d="M0 0l5 4 5-4" stroke="#29b3ec" fill="none"/></svg>info@talloak.com</div>
  </div>
  <div class="abs field" style="top:54px">Name</div>
  <div class="abs field" style="top:80px">Email</div>
  <div class="abs field" style="top:106px;height:46px">Message</div>
  <div class="abs submit">SUBMIT</div>
  <div class="abs f-brand">TALL OAK</div>
  <div class="abs copy">© Copyright 2015 TALLOAK<br>All Rights Reserved</div>
</footer>

</body>
</html>
```